Manuka Honey company needs a Upmarket, Luxury Website!

New Zealand, Taranaki based Manuka Honey company Marumaru Honey is looking for a new website, we are looking for an upmarket, luxury, serious website design. We export the highest quality quality Manuka Honey, straight from the Taranaki region.

Main export markets are Asia & Europe, also New Zealand & Australia.

Looking to have a beautiful, upmarket, serious, luxurious & graphical experience with mobile optimization in mind. Like the use of product staging/mockups

You can use copy from other websites to build the site and we will change the copy after the design is finished.

***Please include 'Honey Product' mockups in website.

*Will add illustrator files in coming days***

Feel free to make website functional in Shopify, Wordpress or WIX

Target Market(s)

Asia, Europe (main markets) New Zealand, Australia (Submarkets)

Coding

Coded - Design and coding required

Number of Pages Required

4 page

Requirements
Must have
• Home, Shop, About Us, Contact Us

Homepage to include:

Our Products
Company Video (video under construction)
What is MGO/UMF
Newsletter Opt-in

***(Not in Order)***

Please include 'Honey Product' mockups in website.
*Will add illustrator files in coming days
Nice to have
• FAQ & Partnership Inquiries (hyperlink in footer)

```html
<!DOCTYPE html>
<html lang="en">
<head>
<meta charset="utf-8">
<title>Marumaru Honey – Our products</title>
<link rel="stylesheet" href="https://fonts.googleapis.com/css2?family=DM+Serif+Display&family=Montserrat:wght@400;500;600&family=Lato:wght@400&display=swap">
<style>
  :root {
    --brown: #5b3a36;
    --brown-text: #6a4844;
    --footer: #5e3c39;
    --footer-bottom: #4e302d;
    --gold: #f6d08f;
    --star: #f5cd8a;
    --white: #ffffff;
    --cream: #f3e7e2;
  }
  * { box-sizing: border-box; margin: 0; padding: 0; }
  html, body { width: 890px; height: 1200px; overflow: hidden; background: var(--white); }
  body { position: relative; font-family: "Montserrat", sans-serif; color: var(--brown); }

  .site-header { position: absolute; left: 0; top: 0; width: 890px; height: 49px; background: var(--white); }
  .brand { position: absolute; display: flex; align-items: center; gap: 6px; font-family: "Montserrat", sans-serif; font-weight: 400; letter-spacing: 2px; text-transform: uppercase; }
  .brand-dot { display: inline-block; border-radius: 50%; }
  .site-header .brand { left: 45px; top: 17px; font-size: 10.5px; color: var(--brown); }
  .site-header .brand-dot { width: 14px; height: 14px; border: 1px solid var(--brown); }
  .main-nav { position: absolute; top: 20px; left: 0; width: 100%; }
  .main-nav a { position: absolute; font-size: 8.6px; color: var(--brown); text-decoration: none; letter-spacing: 0.2px; white-space: nowrap; }
  .header-icons svg { position: absolute; top: 18px; width: 14px; height: 14px; }

  .hero { position: absolute; left: 0; top: 49px; width: 890px; height: 201px;
    background: radial-gradient(ellipse at 45% 20%, #d39a3f 0%, #b2722c 35%, #8e5a33 65%, #a57a5c 100%); }
  .hero h1 { position: absolute; top: 52px; width: 100%; text-align: center; font-family: "DM Serif Display", serif; font-weight: 400; font-size: 44px; color: var(--white); letter-spacing: -0.5px; }
  .hero p { position: absolute; top: 117px; width: 100%; text-align: center; font-size: 17px; color: var(--white); }

  .product { position: absolute; width: 200px; text-align: center; }
  .product-jar { display: block; margin: 0 auto; width: 124px; height: 142px; border-radius: 10px 10px 16px 16px; }
  .product h2 { font-family: "DM Serif Display", serif; font-weight: 400; font-size: 26px; color: var(--brown); margin-top: 12px; line-height: 1; }
  .product p { font-size: 8.6px; line-height: 12.4px; color: var(--brown-text); margin-top: 7px; }
  .product .price { font-family: "Lato", sans-serif; font-size: 13px; color: var(--brown); margin-top: 9px; }
  .stars { display: flex; justify-content: center; gap: 4px; margin-top: 10px; }
  .stars svg { width: 12px; height: 12px; fill: var(--star); }

  .jar-black  { background: linear-gradient(#151515 0 20%, #2b2522 20% 100%); }
  .jar-white  { background: linear-gradient(#151515 0 20%, #2b2522 20% 70%, #f4f1ed 70% 86%, #2b2522 86%); }
  .jar-red    { background: linear-gradient(90deg, #2b2522 0 20%, #f1eee9 20% 75%, #2b2522 75%); }
  .jar-blue   { background: linear-gradient(#151515 0 20%, #1e4b8f 20% 88%, #1b1716 88%); }
  .jar-orange { background: linear-gradient(#151515 0 20%, #c2551f 20% 88%, #1b1716 88%); }
  .jar-purple { background: linear-gradient(#151515 0 20%, #6a2f93 20% 88%, #1b1716 88%); }

  .site-footer { position: absolute; left: 0; top: 1037px; width: 890px; height: 133px; background: var(--footer); color: var(--cream); }
  .site-footer .brand { left: 71px; top: 22px; font-size: 11px; color: var(--cream); }
  .site-footer .brand-dot { width: 16px; height: 16px; border: 1px solid var(--cream); }
  .footer-about { position: absolute; left: 71px; top: 56px; width: 158px; font-size: 7.4px; line-height: 11px; text-align: justify; }
  .footer-col { position: absolute; top: 25px; }
  .footer-col h3 { font-size: 8.6px; font-weight: 600; letter-spacing: 0.4px; margin-bottom: 8px; }
  .footer-col a { display: block; font-size: 8.6px; color: var(--cream); text-decoration: none; line-height: 20.4px; }
  .signup-form { position: absolute; left: 632px; top: 40px; display: flex; gap: 6px; }
  .signup-form .email { width: 141px; height: 24px; border: 1px solid var(--cream); font-size: 8.6px; color: var(--cream); padding: 6px 8px; }
  .signup-form .send { width: 62px; height: 24px; background: var(--gold); color: var(--brown); font-size: 8.6px; font-weight: 500; display: flex; align-items: center; justify-content: center; }
  .social { position: absolute; left: 632px; top: 79px; display: flex; gap: 9px; }
  .social span { width: 21px; height: 21px; border: 1px solid var(--cream); border-radius: 50%; }
  .copyright { position: absolute; left: 0; top: 1170px; width: 890px; height: 30px; background: var(--footer-bottom); color: var(--cream); font-size: 8.6px; text-align: center; line-height: 30px; }
</style>
</head>
<body>

<header class="site-header">
  <div class="brand"><span class="brand-dot"></span>Marumaru Honey</div>
  <nav class="main-nav">
    <a style="left:342px">SHOP</a>
    <a style="left:399px">OUR STORY</a>
    <a style="left:482px">STOCKISTS</a>
    <a style="left:562px">CONTACT US</a>
  </nav>
  <div class="header-icons">
    <svg style="left:736px" viewBox="0 0 24 24" fill="none" stroke="#5b3a36" stroke-width="1.6"><path d="M12 20s-8-5-8-11a4.5 4.5 0 0 1 8-2.8A4.5 4.5 0 0 1 20 9c0 6-8 11-8 11z"/></svg>
    <svg style="left:765px" viewBox="0 0 24 24" fill="none" stroke="#5b3a36" stroke-width="1.6"><circle cx="12" cy="8" r="4"/><path d="M4 21c1-4 4-6 8-6s7 2 8 6z"/></svg>
    <svg style="left:794px" viewBox="0 0 24 24" fill="none" stroke="#5b3a36" stroke-width="1.6"><path d="M5 8h14l-1 13H6z"/><path d="M9 8V6a3 3 0 0 1 6 0v2"/><circle cx="18" cy="19" r="3.5" fill="#d24a3f" stroke="none"/></svg>
  </div>
</header>

<section class="hero" role="img" aria-label="Close-up of honey dripping from a wooden dipper into a glass jar">
  <h1>Our products</h1>
  <p>A Manuka Honey You’ll love from a brand you can trust</p>
</section>

<main>
  <article class="product" style="left:121px; top:320px">
    <div class="product-jar jar-black" role="img" aria-label="Jar of manuka honey with black label"></div>
    <h2>Honey</h2>
    <p>Lorem ipsum dolor sit amet, consectetur<br>adipiscing elit. Ultrices sem amet,<br>lobortis eget cursus pharetra consequat<br>libero ultrices. Aenean ipsum aliquet<br>odio arcu sed ullamcorper.</p>
    <div class="price">$45.90</div>
    <div class="stars"><svg viewBox="0 0 24 24"><path d="M12 2l3 7 7 .6-5.3 4.7 1.6 7.2L12 17.8 5.7 21.5l1.6-7.2L2 9.6 9 9z"/></svg><svg viewBox="0 0 24 24"><path d="M12 2l3 7 7 .6-5.3 4.7 1.6 7.2L12 17.8 5.7 21.5l1.6-7.2L2 9.6 9 9z"/></svg><svg viewBox="0 0 24 24"><path d="M12 2l3 7 7 .6-5.3 4.7 1.6 7.2L12 17.8 5.7 21.5l1.6-7.2L2 9.6 9 9z"/></svg><svg viewBox="0 0 24 24"><path d="M12 2l3 7 7 .6-5.3 4.7 1.6 7.2L12 17.8 5.7 21.5l1.6-7.2L2 9.6 9 9z"/></svg><svg viewBox="0 0 24 24"><path d="M12 2l3 7 7 .6-5.3 4.7 1.6 7.2L12 17.8 5.7 21.5l1.6-7.2L2 9.6 9 9z"/></svg></div>
  </article>

  <article class="product" style="left:351px; top:320px">
    <div class="product-jar jar-white" role="img" aria-label="Jar of manuka honey with black and white label"></div>
    <h2>Honey</h2>
    <p>Lorem ipsum dolor sit amet, consectetur<br>adipiscing elit. Ultrices sem amet,<br>lobortis eget cursus pharetra consequat<br>libero ultrices. Aenean ipsum aliquet<br>odio arcu sed ullamcorper.</p>
    <div class="price">$45.90</div>
    <div class="stars"><svg viewBox="0 0 24 24"><path d="M12 2l3 7 7 .6-5.3 4.7 1.6 7.2L12 17.8 5.7 21.5l1.6-7.2L2 9.6 9 9z"/></svg><svg viewBox="0 0 24 24"><path d="M12 2l3 7 7 .6-5.3 4.7 1.6 7.2L12 17.8 5.7 21.5l1.6-7.2L2 9.6 9 9z"/></svg><svg viewBox="0 0 24 24"><path d="M12 2l3 7 7 .6-5.3 4.7 1.6 7.2L12 17.8 5.7 21.5l1.6-7.2L2 9.6 9 9z"/></svg><svg viewBox="0 0 24 24"><path d="M12 2l3 7 7 .6-5.3 4.7 1.6 7.2L12 17.8 5.7 21.5l1.6-7.2L2 9.6 9 9z"/></svg><svg viewBox="0 0 24 24"><path d="M12 2l3 7 7 .6-5.3 4.7 1.6 7.2L12 17.8 5.7 21.5l1.6-7.2L2 9.6 9 9z"/></svg></div>
  </article>

  <article class="product" style="left:567px; top:320px">
    <div class="product-jar jar-red" role="img" aria-label="Jar of manuka honey with white label and red band"></div>
    <h2>Honey</h2>
    <p>Lorem ipsum dolor sit amet, consectetur<br>adipiscing elit. Ultrices sem amet,<br>lobortis eget cursus pharetra consequat<br>libero ultrices. Aenean ipsum aliquet<br>odio arcu sed ullamcorper.</p>
    <div class="price">$45.90</div>
    <div class="stars"><svg viewBox="0 0 24 24"><path d="M12 2l3 7 7 .6-5.3 4.7 1.6 7.2L12 17.8 5.7 21.5l1.6-7.2L2 9.6 9 9z"/></svg><svg viewBox="0 0 24 24"><path d="M12 2l3 7 7 .6-5.3 4.7 1.6 7.2L12 17.8 5.7 21.5l1.6-7.2L2 9.6 9 9z"/></svg><svg viewBox="0 0 24 24"><path d="M12 2l3 7 7 .6-5.3 4.7 1.6 7.2L12 17.8 5.7 21.5l1.6-7.2L2 9.6 9 9z"/></svg><svg viewBox="0 0 24 24"><path d="M12 2l3 7 7 .6-5.3 4.7 1.6 7.2L12 17.8 5.7 21.5l1.6-7.2L2 9.6 9 9z"/></svg><svg viewBox="0 0 24 24"><path d="M12 2l3 7 7 .6-5.3 4.7 1.6 7.2L12 17.8 5.7 21.5l1.6-7.2L2 9.6 9 9z"/></svg></div>
  </article>

  <article class="product" style="left:121px; top:675px">
    <div class="product-jar jar-blue" role="img" aria-label="Jar of manuka honey with blue label"></div>
    <h2>Honey</h2>
    <p>Lorem ipsum dolor sit amet, consectetur<br>adipiscing elit. Ultrices sem amet,<br>lobortis eget cursus pharetra consequat<br>libero ultrices. Aenean ipsum aliquet<br>odio arcu sed ullamcorper.</p>
    <div class="price">$45.90</div>
    <div class="stars"><svg viewBox="0 0 24 24"><path d="M12 2l3 7 7 .6-5.3 4.7 1.6 7.2L12 17.8 5.7 21.5l1.6-7.2L2 9.6 9 9z"/></svg><svg viewBox="0 0 24 24"><path d="M12 2l3 7 7 .6-5.3 4.7 1.6 7.2L12 17.8 5.7 21.5l1.6-7.2L2 9.6 9 9z"/></svg><svg viewBox="0 0 24 24"><path d="M12 2l3 7 7 .6-5.3 4.7 1.6 7.2L12 17.8 5.7 21.5l1.6-7.2L2 9.6 9 9z"/></svg><svg viewBox="0 0 24 24"><path d="M12 2l3 7 7 .6-5.3 4.7 1.6 7.2L12 17.8 5.7 21.5l1.6-7.2L2 9.6 9 9z"/></svg><svg viewBox="0 0 24 24"><path d="M12 2l3 7 7 .6-5.3 4.7 1.6 7.2L12 17.8 5.7 21.5l1.6-7.2L2 9.6 9 9z"/></svg></div>
  </article>

  <article class="product" style="left:351px; top:675px">
    <div class="product-jar jar-orange" role="img" aria-label="Jar of manuka honey with orange floral label"></div>
    <h2>Honey</h2>
    <p>Lorem ipsum dolor sit amet, consectetur<br>adipiscing elit. Ultrices sem amet,<br>lobortis eget cursus pharetra consequat<br>libero ultrices. Aenean ipsum aliquet<br>odio arcu sed ullamcorper.</p>
    <div class="price">$45.90</div>
    <div class="stars"><svg viewBox="0 0 24 24"><path d="M12 2l3 7 7 .6-5.3 4.7 1.6 7.2L12 17.8 5.7 21.5l1.6-7.2L2 9.6 9 9z"/></svg><svg viewBox="0 0 24 24"><path d="M12 2l3 7 7 .6-5.3 4.7 1.6 7.2L12 17.8 5.7 21.5l1.6-7.2L2 9.6 9 9z"/></svg><svg viewBox="0 0 24 24"><path d="M12 2l3 7 7 .6-5.3 4.7 1.6 7.2L12 17.8 5.7 21.5l1.6-7.2L2 9.6 9 9z"/></svg><svg viewBox="0 0 24 24"><path d="M12 2l3 7 7 .6-5.3 4.7 1.6 7.2L12 17.8 5.7 21.5l1.6-7.2L2 9.6 9 9z"/></svg><svg viewBox="0 0 24 24"><path d="M12 2l3 7 7 .6-5.3 4.7 1.6 7.2L12 17.8 5.7 21.5l1.6-7.2L2 9.6 9 9z"/></svg></div>
  </article>

  <article class="product" style="left:568px; top:675px">
    <div class="product-jar jar-purple" role="img" aria-label="Jar of manuka honey with purple floral label"></div>
    <h2>Honey</h2>
    <p>Lorem ipsum dolor sit amet, consectetur<br>adipiscing elit. Ultrices sem amet,<br>lobortis eget cursus pharetra consequat<br>libero ultrices. Aenean ipsum aliquet<br>odio arcu sed ullamcorper.</p>
    <div class="price">$45.90</div>
    <div class="stars"><svg viewBox="0 0 24 24"><path d="M12 2l3 7 7 .6-5.3 4.7 1.6 7.2L12 17.8 5.7 21.5l1.6-7.2L2 9.6 9 9z"/></svg><svg viewBox="0 0 24 24"><path d="M12 2l3 7 7 .6-5.3 4.7 1.6 7.2L12 17.8 5.7 21.5l1.6-7.2L2 9.6 9 9z"/></svg><svg viewBox="0 0 24 24"><path d="M12 2l3 7 7 .6-5.3 4.7 1.6 7.2L12 17.8 5.7 21.5l1.6-7.2L2 9.6 9 9z"/></svg><svg viewBox="0 0 24 24"><path d="M12 2l3 7 7 .6-5.3 4.7 1.6 7.2L12 17.8 5.7 21.5l1.6-7.2L2 9.6 9 9z"/></svg><svg viewBox="0 0 24 24"><path d="M12 2l3 7 7 .6-5.3 4.7 1.6 7.2L12 17.8 5.7 21.5l1.6-7.2L2 9.6 9 9z"/></svg></div>
  </article>
</main>

<footer class="site-footer">
  <div class="brand"><span class="brand-dot"></span>Marumaru Honey</div>
  <p class="footer-about">Marumaru Honey is a part of a reforestation initiative and is very focused on providing a positive influence on the environment and community.</p>
  <div class="footer-col" style="left:315px">
    <h3>SITEMAP</h3>
    <a>Shop</a><a>Our Story</a><a>Stockists</a><a>Contact Us</a>
  </div>
  <div class="footer-col" style="left:444px">
    <h3>HELP</h3>
    <a>Stock Our Products</a><a>Refund Policy</a><a>Privacy Policy</a><a>Terms &amp; Conditions</a>
  </div>
  <div class="footer-col" style="left:632px">
    <h3>SIGN UP</h3>
  </div>
  <div class="signup-form">
    <div class="email">Enter email</div>
    <div class="send">SEND</div>
  </div>
  <div class="social">
    <span aria-label="Social link 1"></span>
    <span aria-label="Social link 2"></span>
    <span aria-label="Social link 3"></span>
  </div>
</footer>
<div class="copyright">Copyright © 2021 All rights reserved.</div>

</body>
</html>
```